Design Executive Business Acquisitons Brokerage Website

Modern but Professional with the colours black, purple and white. Must convey authenticity, and progressive out-of-square thinking. We are a boutique Business Broking firm located in Brisbane QLD Australia. We market and sell businesses with sales revenue/turnover from Au $1M to $15 M + or have a minimum staff of 15 to 50 staff. Our buyers are generally acquisitions corporate buyers. We need a modern approach but conservative tones. We are serious and experienced. We say it as it is and we get the job done! We sell in the following industries but not limited to, engineering, manufacturing, agriculture, recruitment, transportation, warehousing, services, IT,eCommerce, civil construction,mining, wholesaling, dealerships, MEdical (all), service stations, Management rights, high-end retail, building construction,importing,exporting to name a few.

Target Market(s)

SME Corporate Public & Private exsisting large businesses that are looking to buy through acquisitions

Industry/Entity Type

Coommercial executive Business Sale

Number of Pages Required

5+ page

Font styles to use
Sans Serif

Requirements
Must have
• Serious tones, searchar, NDA form, serious corporate executive feel. Include all corporaate colors,black less whit purples.Corporate Logo
Nice to have
• carosel moving right to left of industry pictures as per above and attached industries
Should not have
• No hand shaking, business people.

```html
<!DOCTYPE html>
<html lang="en">
<head>
<meta charset="utf-8">
<title>Northgate Acquisitions — Business Brokers</title>
<link rel="stylesheet" href="https://fonts.googleapis.com/css2?family=Poppins:ital,wght@0,400;0,500;0,600;0,700;1,500&display=swap">
<style>
:root{
  --purple:#5a2d86;
  --purple-deep:#3f1d63;
  --purple-light:#7b4bb0;
  --ink:#1c1424;
  --text:#6c6675;
  --muted:#9a94a3;
  --line:#e7e3ec;
  --white:#ffffff;
  --soft:#f6f4f9;
  --footer-bar:#2a1540;
}
*{box-sizing:border-box;margin:0;padding:0}
html,body{width:1200px;height:4276px;overflow:hidden}
body{font-family:'Poppins',sans-serif;color:var(--ink);background:var(--white);position:relative}
.abs{position:absolute}
a{color:inherit;text-decoration:none}
.btn{position:absolute;display:flex;align-items:center;justify-content:center;border-radius:24px;font-size:13px;font-weight:600;letter-spacing:.5px;color:var(--white)}
.btn-purple{background:var(--purple)}
.btn-dark{background:var(--ink)}
.btn-white{background:var(--white);color:var(--ink)}
.circle-arrow{position:absolute;width:38px;height:38px;border-radius:50%;background:var(--white);box-shadow:0 3px 10px rgba(40,20,60,.15);display:flex;align-items:center;justify-content:center}
.eyebrow{font-size:17px;font-weight:500;color:var(--ink)}
.section-title{font-size:50px;font-weight:700;line-height:1.1}
.section-title .accent{color:var(--purple)}
p.body{font-size:13.5px;line-height:1.75;color:var(--text)}

/* header */
.brand{left:40px;top:28px;display:flex;align-items:center;gap:10px}
.brand-dot{width:38px;height:38px;border-radius:50%;background:var(--purple)}
.brand-name{font-size:21px;font-weight:700;color:var(--purple-deep);line-height:1;white-space:nowrap}
.nav{left:400px;top:45px;display:flex;gap:28px;font-size:13px;font-weight:500;color:var(--ink);white-space:nowrap}
.nav .active{color:var(--purple)}
.phone-pill{left:1010px;top:32px;width:150px;height:44px;background:var(--purple-deep);border-radius:22px;color:var(--white);font-size:13px;font-weight:500;display:flex;align-items:center;justify-content:center;gap:8px;white-space:nowrap}

/* hero */
.hero{left:0;top:0;width:1200px;height:680px;overflow:hidden}
.hero-photo{position:absolute;left:420px;top:0;width:780px;height:680px;background:linear-gradient(120deg,#eef0f4 0%,#c8ccd6 45%,#8e8aa0 75%,#4a3a62 100%)}
.hero-fade{position:absolute;left:420px;top:0;width:260px;height:680px;background:linear-gradient(90deg,#fff 0%,rgba(255,255,255,0) 100%)}
.hero-kicker{left:44px;top:196px;font-size:19px;font-weight:500}
.hero-title{left:44px;top:228px;font-size:58px;font-weight:700;line-height:1.14}
.hero-title .accent{color:var(--purple)}
.social-row{left:44px;top:626px;display:flex;gap:12px}
.social-row span{width:28px;height:28px;border-radius:50%;border:1.5px solid var(--ink);background:var(--white)}

/* services */
.svc-card{position:absolute;top:952px;width:312px;height:256px;background:var(--white);border-radius:10px;box-shadow:0 6px 24px rgba(50,30,80,.10);padding:40px 34px}
.svc-card.featured{background:linear-gradient(160deg,var(--purple-light),var(--purple-deep));color:var(--white)}
.svc-card h3{font-size:20px;font-weight:600;margin:26px 0 14px}
.svc-card p{font-size:13px;line-height:1.65;color:var(--text)}
.svc-card.featured p{color:#e4d9f0}

/* about */
.about-photo{left:100px;top:1320px;width:500px;height:592px;background:linear-gradient(160deg,#c9d3e2 0%,#8795ad 45%,#3a3550 100%);border-radius:4px}
.about-text{left:660px;top:1382px;width:440px}
.about-text .section-title{font-size:52px;margin:8px 0 24px}

/* for sale band */
.sale-band{left:0;top:1960px;width:1200px;height:840px;background:linear-gradient(160deg,#6a3b96 0%,var(--purple) 45%,var(--purple-deep) 100%)}
.sale-head{left:0;top:2048px;width:1200px;text-align:center;color:var(--white)}
.sale-head .eyebrow{color:var(--white)}
.sale-head .section-title{font-size:48px;margin-top:4px}
.sale-card{position:absolute;top:2172px;width:312px;height:288px;background:var(--white);border-radius:10px;padding:36px 26px}
.sale-card .price{font-size:32px;font-weight:700;color:var(--purple)}
.sale-card .divider{height:1px;background:var(--line);margin:18px 0 20px}
.sale-card h3{font-size:21px;font-weight:600;margin-bottom:10px}
.sale-card p{font-size:13px;line-height:1.65;color:var(--text)}
.sale-card .more{position:absolute;left:26px;bottom:34px;font-size:14px;font-weight:600;display:flex;align-items:center;gap:8px}

/* testimonial */
.testimonial{left:100px;top:2664px;width:1000px;height:288px;background:var(--white);border-radius:10px;box-shadow:0 10px 34px rgba(50,30,80,.14);text-align:center}
.quote-mark{font-size:70px;font-weight:700;color:var(--purple-deep);line-height:1;margin-top:32px;height:58px}
.testimonial blockquote{font-size:25px;font-style:italic;font-weight:500;line-height:1.5;margin:6px auto 0;width:680px}
.avatar{width:46px;height:46px;border-radius:50%;margin:14px auto 6px;background:linear-gradient(135deg,#c7b9a6,#6b5a4c)}
.author{font-size:12px;color:var(--ink)}
.dots{display:flex;justify-content:center;gap:8px;margin-top:14px}
.dots span{width:8px;height:8px;border-radius:50%;background:#c9c3d2}
.dots span.on{background:var(--purple)}

/* blog */
.blog-head{left:0;top:3156px;width:1200px;text-align:center}
.blog-card{position:absolute;top:3288px;width:312px}
.blog-img{height:248px;border-radius:4px}
.blog-card h3{font-size:19px;font-weight:600;margin-top:18px;white-space:nowrap}
.blog-card .rule{width:60px;height:2px;background:var(--purple);margin:10px 0 8px}
.blog-card .date{font-size:12px;color:var(--muted)}
.blog-card p{font-size:13px;line-height:1.6;color:var(--text);margin-top:10px}
.blog-card .more{font-size:13px;font-weight:600;margin-top:16px;display:block}

/* footer */
.site-footer{color:var(--white)}
.footer{left:0;top:3820px;width:1200px;height:412px;background:linear-gradient(160deg,#5d2f8a 0%,var(--purple-deep) 100%)}
.newsletter{left:100px;top:3904px;display:flex;align-items:center;gap:18px;font-size:25px;font-weight:500;color:var(--white);white-space:nowrap}
.news-form{left:620px;top:3902px;width:480px;height:48px;background:var(--white);border-radius:24px;padding:0 6px 0 22px;display:flex;align-items:center;justify-content:space-between;font-size:13px;color:var(--muted)}
.news-form .sub{background:var(--ink);color:var(--white);height:38px;width:118px;border-radius:19px;display:flex;align-items:center;justify-content:center;font-weight:500}
.footer-rule{left:100px;top:3992px;width:1000px;height:1px;background:rgba(255,255,255,.18)}
.fcol{position:absolute;top:4024px;font-size:13px;line-height:1.9;color:#e3d8ee}
.fcol h4{font-size:17px;font-weight:600;color:var(--white);margin-bottom:10px}
.fbrand{display:flex;align-items:center;gap:10px;margin-bottom:18px;white-space:nowrap}
.fbrand span.dot{width:30px;height:30px;border-radius:50%;background:var(--white);flex:none}
.fbrand b{font-size:18px;font-weight:700;color:var(--white)}
.contact-line{display:flex;align-items:center;gap:10px;white-space:nowrap}
.fsocial{display:flex;gap:10px;margin-bottom:14px}
.fsocial span{width:32px;height:32px;border-radius:50%;border:1.5px solid rgba(255,255,255,.7)}
.bottom-bar{left:0;top:4232px;width:1200px;height:44px;background:var(--footer-bar);color:#cfc3dc;font-size:12px;display:flex;align-items:center;justify-content:space-between;padding:0 100px}
.bottom-bar nav{display:flex;gap:40px}
</style>
</head>
<body>

<!-- HERO -->
<section class="hero abs">
  <div class="hero-photo" role="img" aria-label="Photo of a confident team of brokers in business attire"></div>
  <div class="hero-fade"></div>
</section>

<header>
  <div class="brand abs"><span class="brand-dot"></span><span class="brand-name">Northgate Acquisitions</span></div>
  <nav class="nav abs">
    <a class="active">Home</a><a>Our Services</a><a>About Us</a><a>Business For Sale</a><a>Blog</a><a>Contact Us</a>
  </nav>
  <div class="phone-pill abs">
    <svg width="14" height="14" viewBox="0 0 24 24" fill="#fff"><path d="M6.6 10.8a15 15 0 0 0 6.6 6.6l2.2-2.2a1 1 0 0 1 1-.25 11.4 11.4 0 0 0 3.6.57 1 1 0 0 1 1 1V20a1 1 0 0 1-1 1A17 17 0 0 1 3 4a1 1 0 0 1 1-1h3.5a1 1 0 0 1 1 1c0 1.250.2 2.45.57 3.6a1 1 0 0 1-.25 1z"/></svg>
    +61 400 555 210
  </div>
</header>

<div class="hero-kicker abs">#1 Broker in the Country</div>
<h1 class="hero-title abs"><span class="accent">Sell Your Business</span><br>&amp; Start Your<br>Next Adventure</h1>
<a class="btn btn-purple" style="left:44px;top:472px;width:186px;height:44px">READ MORE</a>
<a class="btn btn-dark" style="left:244px;top:472px;width:186px;height:44px">CONTACT US</a>
<div class="social-row abs"><span></span><span></span><span></span><span></span></div>
<div class="circle-arrow" style="left:1052px;top:624px"><svg width="14" height="14" viewBox="0 0 24 24"><path d="M15 5l-7 7 7 7" stroke="#1c1424" stroke-width="2.5" fill="none"/></svg></div>
<div class="circle-arrow" style="left:1102px;top:624px;background:var(--ink)"><svg width="14" height="14" viewBox="0 0 24 24"><path d="M9 5l7 7-7 7" stroke="#fff" stroke-width="2.5" fill="none"/></svg></div>

<!-- SERVICES -->
<div class="abs" style="left:100px;top:760px">
  <div class="eyebrow">What We Do</div>
  <h2 class="section-title" style="margin-top:2px"><span class="accent">Our</span> Services</h2>
  <p class="body" style="width:560px;margin-top:12px">Lorem ipsum dolor sit amet, consectetur adipiscing elit, sed do eiusmod tempor incididunt ut labore et dolore magna aliqua. Ut enim ad minim veniam, quis nostrud exercitation ullamco laboris.</p>
</div>
<a class="btn btn-purple" style="left:916px;top:860px;width:184px;height:42px">READ MORE</a>

<div class="circle-arrow" style="left:44px;top:1061px"><svg width="14" height="14" viewBox="0 0 24 24"><path d="M15 5l-7 7 7 7" stroke="#1c1424" stroke-width="2.5" fill="none"/></svg></div>
<div class="circle-arrow" style="left:1118px;top:1061px"><svg width="14" height="14" viewBox="0 0 24 24"><path d="M9 5l7 7-7 7" stroke="#1c1424" stroke-width="2.5" fill="none"/></svg></div>

<article class="svc-card" style="left:100px">
  <svg width="46" height="46" viewBox="0 0 48 48" fill="none" stroke="#5a2d86" stroke-width="2.5"><rect x="6" y="10" width="22" height="32"/><rect x="28" y="20" width="14" height="22"/><path d="M12 17h4M20 17h4M12 25h4M20 25h4M12 33h4M20 33h4M33 27h4M33 34h4"/></svg>
  <h3>Selling Business</h3>
  <p>Lorem ipsum dolor sit amet, consectetur adipiscing elit, sed do eiusmod tempor incididunt ut labore et dolore.</p>
</article>
<article class="svc-card featured" style="left:444px">
  <svg width="46" height="46" viewBox="0 0 48 48"><text x="12" y="40" font-family="Poppins,sans-serif" font-size="40" font-weight="600" fill="#fff">$</text></svg>
  <h3>Business Valuation</h3>
  <p>Lorem ipsum dolor sit amet, consectetur adipiscing elit, sed do eiusmod tempor incididunt ut labore et dolore.</p>
</article>
<article class="svc-card" style="left:788px">
  <svg width="46" height="46" viewBox="0 0 48 48" fill="none" stroke="#5a2d86" stroke-width="2.5"><path d="M4 30h8l8 6h14a3 3 0 0 0 0-6H24M12 42V26M26 8v14M22 12a4 3 0 0 1 4-3 4 3 0 0 1 4 3c0 4-8 2-8 6a4 3 0 0 0 4 3 4 3 0 0 0 4-3"/></svg>
  <h3>Business Acquisition</h3>
  <p>Lorem ipsum dolor sit amet, consectetur adipiscing elit, sed do eiusmod tempor incididunt ut labore et dolore.</p>
</article>

<!-- ABOUT -->
<div class="about-photo abs" role="img" aria-label="Photo of three brokers standing in front of a glass office building"></div>
<div class="about-text abs">
  <div class="eyebrow">Who We Are</div>
  <h2 class="section-title"><span class="accent">Not Your Typical</span><br>Broker Firm</h2>
  <p class="body">Lorem ipsum dolor sit amet, consectetur adipiscing elit, sed do eiusmod tempor incididunt ut labore et dolore magna aliqua. Ut enim ad minim veniam, quis nostrud.</p>
  <p class="body" style="margin-top:14px">Exercitation ullamco laboris nisi ut aliquip ex ea commodo consequat. Duis aute irure dolor in reprehenderit in voluptate velit esse cillum dolore eu fugiat nulla pariatur. Excepteur sint occaecat cupidatat non proident, sunt in culpa qui officia.</p>
</div>
<a class="btn btn-purple" style="left:660px;top:1752px;width:184px;height:42px">READ MORE</a>

<!-- BUSINESS FOR SALE -->
<section class="sale-band abs"></section>
<div class="sale-head abs">
  <div class="eyebrow">Lorum Ipsum</div>
  <h2 class="section-title">Business For Sale</h2>
</div>
<div class="circle-arrow" style="left:44px;top:2297px"><svg width="14" height="14" viewBox="0 0 24 24"><path d="M15 5l-7 7 7 7" stroke="#1c1424" stroke-width="2.5" fill="none"/></svg></div>
<div class="circle-arrow" style="left:1118px;top:2297px"><svg width="14" height="14" viewBox="0 0 24 24"><path d="M9 5l7 7-7 7" stroke="#1c1424" stroke-width="2.5" fill="none"/></svg></div>

<article class="sale-card" style="left:100px">
  <div class="price">$68,000,000</div><div class="divider"></div>
  <h3>Geo Drilling Corporation</h3>
  <p>Lorem ipsum dolor sit amet, consectetur adipiscing elit, sed do eiusmod tempor incididunt ut labore.</p>
  <a class="more">Read More <svg width="16" height="12" viewBox="0 0 16 12"><path d="M0 6h14M9 1l5 5-5 5" stroke="#1c1424" stroke-width="2" fill="none"/></svg></a>
</article>
<article class="sale-card" style="left:444px">
  <div class="price">$2,000,000</div><div class="divider"></div>
  <h3>Restaurant Chain</h3>
  <p>Lorem ipsum dolor sit amet, consectetur adipiscing elit, sed do eiusmod tempor incididunt ut labore.</p>
  <a class="more">Read More <svg width="16" height="12" viewBox="0 0 16 12"><path d="M0 6h14M9 1l5 5-5 5" stroke="#1c1424" stroke-width="2" fill="none"/></svg></a>
</article>
<article class="sale-card" style="left:788px">
  <div class="price">$2,800,000</div><div class="divider"></div>
  <h3>Ball Manufacturer</h3>
  <p>Lorem ipsum dolor sit amet, consectetur adipiscing elit, sed do eiusmod tempor incididunt ut labore.</p>
  <a class="more">Read More <svg width="16" height="12" viewBox="0 0 16 12"><path d="M0 6h14M9 1l5 5-5 5" stroke="#1c1424" stroke-width="2" fill="none"/></svg></a>
</article>
<a class="btn btn-white" style="left:508px;top:2528px;width:184px;height:40px">VIEW MORE</a>

<!-- TESTIMONIAL -->
<section class="testimonial abs">
  <div class="quote-mark">&#8221;</div>
  <blockquote>I've met a lot of business brokers... no one's going to work harder for you than this group</blockquote>
  <div class="avatar" role="img" aria-label="Portrait of the client"></div>
  <div class="author">Daniel Harper - Business Owner</div>
  <div class="dots"><span class="on"></span><span></span><span></span><span></span></div>
</section>

<!-- BLOG -->
<div class="blog-head abs">
  <div class="eyebrow">Our Blog</div>
  <h2 class="section-title" style="font-size:50px;margin-top:2px"><span class="accent">News</span> &amp; Events</h2>
</div>
<div class="circle-arrow" style="left:44px;top:3393px"><svg width="14" height="14" viewBox="0 0 24 24"><path d="M15 5l-7 7 7 7" stroke="#1c1424" stroke-width="2.5" fill="none"/></svg></div>
<div class="circle-arrow" style="left:1118px;top:3393px"><svg width="14" height="14" viewBox="0 0 24 24"><path d="M9 5l7 7-7 7" stroke="#1c1424" stroke-width="2.5" fill="none"/></svg></div>

<article class="blog-card" style="left:100px">
  <div class="blog-img" role="img" aria-label="Photo of a business team in front of an office" style="background:linear-gradient(160deg,#d7dde6,#8290a6 55%,#2f2c40)"></div>
  <h3>Lorem ipsum dolor sit amet...</h3><div class="rule"></div>
  <div class="date">12 - June - 2022</div>
  <p>Lorem ipsum dolor sit amet, consectetur adipiscing elit, sed do eiusmod tempor incididunt ut labore.</p>
  <a class="more">Read More</a>
</article>
<article class="blog-card" style="left:444px">
  <div class="blog-img" role="img" aria-label="Photo of colleagues meeting in a bright office" style="background:linear-gradient(160deg,#e8e2da,#a99b8c 55%,#4a4050)"></div>
  <h3>Lorem ipsum dolor sit amet...</h3><div class="rule"></div>
  <div class="date">12 - June - 2022</div>
  <p>Lorem ipsum dolor sit amet, consectetur adipiscing elit, sed do eiusmod tempor incididunt ut labore.</p>
  <a class="more">Read More</a>
</article>
<article class="blog-card" style="left:788px">
  <div class="blog-img" role="img" aria-label="Photo of a group of executives" style="background:linear-gradient(160deg,#eef0f3,#b3b7c2 55%,#2c2634)"></div>
  <h3>Lorem ipsum dolor sit amet...</h3><div class="rule"></div>
  <div class="date">12 - June - 2022</div>
  <p>Lorem ipsum dolor sit amet, consectetur adipiscing elit, sed do eiusmod tempor incididunt ut labore.</p>
  <a class="more">Read More</a>
</article>

<!-- FOOTER -->
<footer class="site-footer">
  <div class="footer abs"></div>
  <div class="newsletter abs">
    <svg width="38" height="28" viewBox="0 0 38 28" fill="none" stroke="#fff" stroke-width="2.5"><rect x="2" y="2" width="34" height="24" rx="2"/><path d="M2 4l17 12L36 4"/></svg>
    Subscribe to our Newsletter
  </div>
  <div class="news-form abs"><span>Your Email</span><span class="sub">Subscribe</span></div>
  <div class="footer-rule abs"></div>

  <div class="fcol" style="left:100px;width:270px">
    <div class="fbrand"><span class="dot"></span><b>Northgate Acquisitions</b></div>
    <div class="contact-line"><svg width="12" height="12" viewBox="0 0 24 24" fill="#fff"><path d="M6.6 10.8a15 15 0 0 0 6.6 6.6l2.2-2.2a1 1 0 0 1 1-.25 11.4 11.4 0 0 0 3.6.57 1 1 0 0 1 1 1V20a1 1 0 0 1-1 1A17 17 0 0 1 3 4a1 1 0 0 1 1-1h3.5a1 1 0 0 1 1 1c0 1.25.2 2.45.57 3.6a1 1 0 0 1-.25 1z"/></svg>+61 400 555 210</div>
    <div class="contact-line"><svg width="12" height="10" viewBox="0 0 24 18" fill="none" stroke="#fff" stroke-width="2.5"><rect x="1" y="1" width="22" height="16"/><path d="M1 2l11 8 11-8"/></svg>hello@northgate-acq.example</div>
    <div class="contact-line"><svg width="12" height="14" viewBox="0 0 24 28" fill="#fff"><path d="M12 0a10 10 0 0 0-10 10c0 8 10 18 10 18s10-10 10-18A10 10 0 0 0 12 0zm0 14a4 4 0 1 1 0-8 4 4 0 0 1 0 8z"/></svg>42 Harbour Lane, Brisbane</div>
  </div>
  <div class="fcol" style="left:390px">
    <h4>Our Services</h4>
    Selling a Business<br>Business Valuation<br>Business Acquisition<br>Capital Raising<br>Business Advisory
  </div>
  <div class="fcol" style="left:648px">
    <h4>Usefull Link</h4>
    Home<br>About Us<br>Business For Sale<br>Blog<br>Contact Us
  </div>
  <div class="fcol" style="left:880px;width:220px">
    <h4>Follow US</h4>
    <div class="fsocial"><span></span><span></span><span></span><span></span></div>
    Lorem ipsum dolor sit amet, consectetur adipiscing elit, sed do eiusmod tempor.
  </div>
  <div class="bottom-bar abs">
    <span>2022 All rights reserved</span>
    <nav><a>Privacy Policy</a><a>Terms &amp; Conditions</a></nav>
  </div>
</footer>

</body>
</html>
```